Dale Hornsby's Swingcraft Big Band — Hot & Sticky ------ CD Cover Art (and Disc Art)

Need a front cover jacket and a disc design for a fantastic all-pro big band (jazz/funk/reggae) CD. We really want to use a group photo somehow since so many of the band members are world famous, LA's finest studio musicians with mostly original music arranged by the biggest names in jazz. Playful, fun, lighthearted, tasteful arrangements with world class soloists.

Target Market(s)

Music/Jazz/Big band enthusiasts; other musicians

Other font styles liked:
• See uploaded file #4

Colors

Designer to choose colors to be used in the design.

Requirements
Must have
• Legibility . . . must be easy to read and not crowded or cluttered. Font idea below (A Quiet Night Beneath The Tangled Pines) is for feel and flavor. It is absolutely not necessary to match if you have something you like better.
Nice to have
• Colorful but not tacky. Maybe a play on the CD title, Hot and Sticky?

```html
<!DOCTYPE html>
<html lang="en">
<head>
<meta charset="utf-8">
<title>Hot and Sticky — CD Packaging</title>
<link href="https://fonts.googleapis.com/css2?family=Fredoka:wght@700&family=Montserrat:wght@500;800&display=swap" rel="stylesheet">
<style>
  :root {
    --backdrop: #e3dfca;
    --paper: #ffffff;
    --ink-deep: #1d3556;
    --ink-mid: #3f6f9f;
    --ink-light: #8fb2d4;
    --ink-pale: #d7e4f0;
    --label-black: #111111;
    --title-white: #ffffff;
    --photo-dark: #3a3d42;
    --photo-light: #8b8f95;
  }
  * { box-sizing: border-box; margin: 0; padding: 0; }
  html, body { width: 1200px; height: 720px; overflow: hidden; }
  body { background: var(--backdrop); position: relative; font-family: "Montserrat", sans-serif; }

  .wash {
    position: absolute; inset: 0;
    background:
      radial-gradient(circle at 25% 22%, var(--ink-deep) 0 8%, transparent 22%),
      radial-gradient(circle at 70% 30%, var(--ink-deep) 0 6%, transparent 20%),
      radial-gradient(circle at 45% 45%, var(--ink-mid) 0 12%, transparent 30%),
      radial-gradient(circle at 85% 55%, var(--ink-mid) 0 8%, transparent 24%),
      radial-gradient(circle at 15% 60%, var(--ink-mid) 0 8%, transparent 24%),
      linear-gradient(180deg, var(--ink-light) 0%, var(--ink-mid) 35%, var(--ink-light) 60%, var(--ink-pale) 75%, var(--paper) 88%);
  }

  .title {
    position: absolute;
    font-family: "Fredoka", sans-serif; font-weight: 700;
    color: var(--title-white); line-height: 0.9; text-transform: uppercase;
  }
  .title .line-small { display: block; font-size: 0.5em; letter-spacing: 0.02em; }
  .title .line-big { display: block; font-size: 1em; }

  .label-name {
    position: absolute;
    display: flex; align-items: center; gap: 4px;
    font-family: "Montserrat", sans-serif; font-weight: 800;
    color: var(--label-black); font-size: 10px; letter-spacing: 0.04em; text-transform: uppercase;
    white-space: nowrap;
  }
  .label-name .mark { width: 8px; height: 8px; background: var(--label-black); }

  /* Open digipak */
  .digipak { position: absolute; left: 60px; top: 40px; width: 660px; height: 330px; display: flex; }
  .panel { position: relative; width: 330px; height: 330px; overflow: hidden; background: var(--paper); }
  .panel-back .title { left: 40px; top: 110px; font-size: 64px; }
  .panel-back .label-name { left: 130px; bottom: 36px; }
  .panel-front { border-left: 1px solid rgba(0,0,0,0.08); }
  .panel-front .title { left: 60px; top: 40px; font-size: 62px; }
  .panel-front .featuring {
    position: absolute; left: 40px; top: 170px; width: 260px;
    font-size: 9px; font-weight: 500; line-height: 1.4; color: var(--title-white);
    text-transform: uppercase; letter-spacing: 0.03em;
  }
  .panel-front .label-name { right: 30px; bottom: 36px; }

  /* Disc */
  .disc {
    position: absolute; left: 150px; top: 390px; width: 300px; height: 300px;
    border-radius: 50%; overflow: hidden; background: var(--paper);
    box-shadow: 0 0 0 6px var(--paper), 0 2px 8px rgba(0,0,0,0.15);
  }
  .disc .wash {
    background:
      radial-gradient(circle at 30% 25%, var(--ink-deep) 0 8%, transparent 24%),
      radial-gradient(circle at 75% 30%, var(--ink-mid) 0 10%, transparent 26%),
      linear-gradient(180deg, var(--ink-light) 0%, var(--ink-mid) 30%, var(--ink-pale) 55%, var(--paper) 70%);
  }
  .disc .title { left: 48px; top: 36px; font-size: 40px; }
  .disc .hub {
    position: absolute; left: 50%; top: 50%; width: 44px; height: 44px; margin: -22px 0 0 -22px;
    border-radius: 50%; background: var(--backdrop); box-shadow: 0 0 0 14px rgba(255,255,255,0.6);
  }
  .disc .label-name { right: 60px; bottom: 56px; }

  /* Booklet */
  .booklet { position: absolute; left: 790px; top: 290px; width: 340px; height: 340px; overflow: hidden; background: var(--paper); box-shadow: 0 2px 8px rgba(0,0,0,0.15); }
  .booklet .wash {
    background:
      radial-gradient(circle at 20% 25%, var(--ink-deep) 0 8%, transparent 22%),
      radial-gradient(circle at 80% 20%, var(--ink-deep) 0 6%, transparent 20%),
      linear-gradient(180deg, var(--ink-light) 0%, var(--ink-mid) 45%, var(--ink-light) 100%);
  }
  .booklet .title { left: 70px; top: 40px; font-size: 60px; }
  .booklet .band-photo {
    position: absolute; left: 0; right: 0; bottom: 0; height: 170px;
    background: linear-gradient(180deg, transparent 0%, var(--photo-light) 25%, var(--photo-dark) 100%);
  }
</style>
</head>
<body>

  <section class="digipak">
    <div class="panel panel-back">
      <div class="wash" role="img" aria-label="Blue watercolour ink wash fading to white"></div>
      <h2 class="title"><span class="line-small">Hot and</span><span class="line-big">Sticky</span></h2>
      <div class="label-name"><span class="mark"></span>Sly Owl Records</div>
    </div>
    <div class="panel panel-front">
      <div class="wash" role="img" aria-label="Blue watercolour ink wash fading to white"></div>
      <h1 class="title"><span class="line-small">Hot and</span><span class="line-big">Sticky</span></h1>
      <p class="featuring">Featuring artists like Greta Holloway, Marcus Fenwick, Iris Quayle, Oren Bastable and Lydia Crane</p>
      <div class="label-name"><span class="mark"></span>Sly Owl Records</div>
    </div>
  </section>

  <section class="disc">
    <div class="wash" role="img" aria-label="Blue watercolour ink wash fading to white"></div>
    <h2 class="title"><span class="line-small">Hot and</span><span class="line-big">Sticky</span></h2>
    <div class="hub"></div>
    <div class="label-name"><span class="mark"></span>Sly Owl Records</div>
  </section>

  <section class="booklet">
    <div class="wash" role="img" aria-label="Blue watercolour ink wash"></div>
    <h2 class="title"><span class="line-small">Hot and</span><span class="line-big">Sticky</span></h2>
    <div class="band-photo" role="img" aria-label="Black and white group photo of the big band with their instruments"></div>
  </section>

</body>
</html>
```